landscape and garden design business card

I would like a business card designed for my landscape and garden design company, Wrenfield Landscapes. We are located in Colorado. I would like to include our logo, contact info, and social media/web site address or QR code. Looking for an organic, flowing design that incorporates our logo.

Target Market(s)

Homeowners and businesses that need garden and landscape design

Contact Information for Business Card

Would like it to say landscape and garden design

Requirements
Must have
• Landscape and garden design

```html
<!DOCTYPE html>
<html lang="en">
<head>
<meta charset="UTF-8">
<title>Wrenfield Landscapes – Business Card</title>
<link href="https://fonts.googleapis.com/css2?family=Montserrat:wght@700&family=Poppins:wght@300;400&display=swap" rel="stylesheet">
<style>
  :root {
    --forest: #243230;
    --stone: #b8b6a8;
    --paper: #ffffff;
    --ink: #243230;
    --text: #2c2c2c;
    --backdrop: #1c1e1f;
  }
  * { margin: 0; padding: 0; box-sizing: border-box; }
  html, body { width: 1200px; height: 900px; overflow: hidden; }
  body {
    background: var(--backdrop);
    font-family: "Poppins", sans-serif;
    position: relative;
  }
  .card {
    position: absolute;
    left: 260px;
    width: 680px;
    height: 388px;
    overflow: hidden;
  }
  .card--front { top: 46px; background: var(--forest); }
  .card--back { top: 466px; background: var(--paper); }

  /* Front */
  .brand {
    position: absolute;
    left: 0; right: 0; top: 62px;
    display: flex; flex-direction: column; align-items: center;
  }
  .brand__disc {
    width: 110px; height: 110px; border-radius: 50%;
    background: var(--stone);
  }
  .brand__name {
    margin-top: 16px;
    font-family: "Poppins", sans-serif;
    font-weight: 300;
    font-size: 34px;
    line-height: 44px;
    letter-spacing: 1px;
    color: var(--stone);
  }
  .brand__tagline {
    margin-top: 4px;
    font-family: "Poppins", sans-serif;
    font-weight: 300;
    font-size: 13px;
    letter-spacing: 3px;
    text-transform: uppercase;
    color: var(--stone);
  }
  .social {
    position: absolute;
    left: 0; right: 0; top: 322px;
    display: flex; justify-content: center; gap: 38px;
  }
  .social__dot {
    width: 20px; height: 20px; border-radius: 50%;
    background: var(--stone);
  }

  /* Back */
  .night-sky { position: absolute; left: 0; top: 0; }
  .person {
    position: absolute; left: 420px; top: 58px;
  }
  .person__name {
    font-family: "Montserrat", sans-serif;
    font-weight: 700;
    font-size: 22px;
    letter-spacing: 1.5px;
    color: var(--ink);
  }
  .person__role {
    font-weight: 300;
    font-size: 15px;
    color: var(--text);
    margin-top: 2px;
  }
  .person__rule {
    width: 52px; height: 1px; background: var(--ink);
    margin-top: 10px;
  }
  .contact {
    position: absolute; left: 406px; top: 222px;
    font-size: 16px; color: var(--text); font-weight: 400;
    list-style: none;
  }
  .contact__address { line-height: 26px; margin-bottom: 14px; }
  .contact__item {
    display: flex; align-items: center; gap: 10px;
    line-height: 24px;
  }
  .contact__icon { width: 13px; height: 13px; flex: none; }
</style>
</head>
<body>

  <section class="card card--front" aria-label="Card front">
    <div class="brand">
      <div class="brand__disc"></div>
      <div class="brand__name">Wrenfield Landscapes</div>
      <div class="brand__tagline">Landscape and garden design</div>
    </div>
    <div class="social" aria-label="Social media links">
      <span class="social__dot"></span>
      <span class="social__dot"></span>
      <span class="social__dot"></span>
    </div>
  </section>

  <section class="card card--back" aria-label="Card back">
    <svg class="night-sky" width="680" height="388" viewBox="0 0 680 388"
         role="img" aria-label="Night sky illustration with crescent moon, stars and pine tree silhouettes">
      <circle cx="100" cy="240" r="270" fill="var(--forest)"/>
    </svg>

    <div class="person">
      <div class="person__name">DANIEL HARLOW</div>
      <div class="person__role">Development Manager Officer</div>
      <div class="person__rule"></div>
    </div>

    <ul class="contact">
      <li class="contact__address">412 Aspen Ridge Road<br>Suite 210, Boulder, CO 80302</li>
      <li class="contact__item">
        <svg class="contact__icon" viewBox="0 0 24 24" aria-hidden="true"><path fill="var(--text)" d="M6.6 10.8a15.1 15.1 0 0 0 6.6 6.6l2.2-2.2a1 1 0 0 1 1-.25 11.4 11.4 0 0 0 3.6.57 1 1 0 0 1 1 1V20a1 1 0 0 1-1 1A17 17 0 0 1 3 4a1 1 0 0 1 1-1h3.5a1 1 0 0 1 1 1c0 1.25.2 2.45.57 3.57a1 1 0 0 1-.25 1z"/></svg>
        720-555-0184
      </li>
      <li class="contact__item">
        <svg class="contact__icon" viewBox="0 0 24 24" aria-hidden="true"><path fill="var(--text)" d="M2 5h20v14H2z"/><path fill="none" stroke="#fff" stroke-width="2" d="M2 6l10 7 10-7"/></svg>
        daniel@wrenfield.com
      </li>
      <li class="contact__item">
        <svg class="contact__icon" viewBox="0 0 24 24" aria-hidden="true"><g fill="none" stroke="var(--text)" stroke-width="1.8"><circle cx="12" cy="12" r="10"/><ellipse cx="12" cy="12" rx="4" ry="10"/><path d="M2 12h20"/></g></svg>
        wrenfield.com
      </li>
    </ul>
  </section>

</body>
</html>
```